Maplebright Savings Spree Promotional Postcard

I would like a postcard designed for a credit card balance transfer promotion.

The title for this promotion is "Maplebright savings spree".

(This paragraph should not be used word for word) Credit Card rates are on the rise since the Federal Prime Rate increase. I want to promote a non-variable rate credit card with rates as low as 7.9% APR* and free balance transfers. Simple, straightforward card with a low rate. There is no intro APR, always a great rate.

Below is some sample content options to highlight:
$0 Annual Fee
$0 Balance Transfer Fee
No Teaser, No Intro, just a great rate

Not only could you cut your interest rate in half, but you will also save hundreds of dollars by not paying any balance transfer fees.

Apply Today! www.tallowmerefin.org

Target Market(s)

Ages 25-45

Industry/Entity Type

Credit Card

Requirements
Must have
• Required disclaimer: *Annual Percentage Rate. 7.9% is the preferred rate based on qualifying credit. (teeny tiny disclaimer on front of card where rate is being advertised)
• Tagline: When you need OPTIONS ... (should be placed on back of postcard by credit union name, address, and logo)

```html
<!DOCTYPE html>
<html lang="en">
<head>
<meta charset="utf-8">
<title>Maplebright Savings Spree Postcard</title>
<link href="https://fonts.googleapis.com/css2?family=Lobster&family=Ubuntu:wght@400;500;700&display=swap" rel="stylesheet">
<style>
  :root {
    --red-deep: #b30f27;
    --red: #d8152f;
    --red-bright: #e8283f;
    --wine: #9b1b30;
    --grey-text: #6d6e71;
    --ink: #3a3a3c;
    --band: #e6e7e8;
    --charcoal: #3d3d3f;
    --rule: #a7a9ac;
    --page: #eeeeee;
    --white: #ffffff;
  }
  * { box-sizing: border-box; margin: 0; padding: 0; }
  html, body { width: 865px; height: 1200px; overflow: hidden; }
  body { background: var(--page); font-family: "Ubuntu", sans-serif; position: relative; }

  .postcard { position: absolute; background: var(--white); overflow: hidden; box-shadow: 0 2px 6px rgba(0,0,0,.15); }

  /* Front */
  .front { left: 71px; top: 71px; width: 642px; height: 496px; }
  .front-header {
    position: absolute; left: 0; top: 0; width: 100%; height: 109px;
    background: linear-gradient(90deg, var(--red-deep), var(--red-bright) 60%, var(--red));
  }
  .brand-name { position: absolute; left: 26px; top: 40px; color: var(--white); font-size: 21px; font-weight: 500; }
  .promo-title {
    position: absolute; right: 26px; top: 28px; color: var(--white);
    font-family: "Lobster", cursive; font-size: 37px; font-weight: 400;
  }
  .photo { position: absolute; left: 0; top: 0; width: 642px; height: 496px; }
  .intro { position: absolute; left: 334px; top: 140px; color: var(--grey-text); font-size: 16px; line-height: 1.3; }
  .feature-band { position: absolute; left: 300px; top: 195px; width: 342px; height: 153px; background: var(--band); }
  .feature-list { position: absolute; left: 356px; top: 210px; list-style: none; color: var(--wine); font-weight: 500; font-size: 15px; line-height: 1.15; }
  .feature-list li { position: relative; margin-bottom: 12px; }
  .feature-list svg { position: absolute; left: -21px; top: 4px; }
  .savings-copy { position: absolute; left: 364px; top: 364px; width: 262px; color: var(--ink); font-size: 11px; line-height: 1.35; }
  .disclaimer { position: absolute; left: 424px; top: 435px; color: var(--grey-text); font-size: 6.5px; }
  .front-footer {
    position: absolute; left: 300px; top: 454px; width: 342px; height: 42px;
    background: linear-gradient(90deg, var(--red-deep), var(--red-bright));
    color: var(--white); font-size: 15px; padding: 12px 0 0 56px;
  }

  /* Back */
  .back { left: 156px; top: 632px; width: 640px; height: 496px; }
  .tagline-block {
    position: absolute; left: 0; top: 0; width: 347px; height: 123px;
    background: linear-gradient(90deg, var(--red-deep), var(--red-bright));
    color: var(--white); font-size: 20px; font-weight: 500; text-align: center; line-height: 1.55; padding-top: 27px;
  }
  .brand-block { position: absolute; left: 0; top: 129px; width: 347px; height: 150px; background: var(--band); display: flex; align-items: center; justify-content: center; }
  .brand-block .brand-name { position: static; color: var(--ink); font-size: 30px; }
  .apply-block { position: absolute; left: 0; top: 285px; width: 347px; height: 67px; background: var(--charcoal); color: var(--white); font-size: 14px; padding: 26px 0 0 46px; }
  .address { position: absolute; left: 363px; top: 26px; color: var(--ink); font-size: 12px; font-weight: 500; line-height: 1.3; }
  .phone { position: absolute; left: 363px; top: 84px; color: var(--grey-text); font-size: 12.5px; font-weight: 500; display: flex; align-items: center; gap: 8px; }
  .stamp-box { position: absolute; left: 546px; top: 21px; width: 77px; height: 54px; border: 1.5px solid var(--rule); }
  .mail-line { position: absolute; left: 388px; width: 237px; height: 0; border-top: 1.5px solid var(--rule); }
</style>
</head>
<body>

<section class="postcard front">
  <svg class="photo" viewBox="0 0 642 496" aria-hidden="true">
    <defs>
      <linearGradient id="photoTone" x1="0" y1="0" x2="0" y2="1">
        <stop offset="0" stop-color="#dfe3e4"/>
        <stop offset=".55" stop-color="#e9e6e3"/>
        <stop offset=".8" stop-color="#c1506a"/>
        <stop offset="1" stop-color="#8f8a86"/>
      </linearGradient>
    </defs>
    <path d="M-10,100 Q140,100 262,118 Q345,200 337,308 Q330,420 273,506 L-10,506 Z" fill="var(--white)"/>
    <path d="M262,118 Q345,200 337,308 Q330,420 273,506" fill="none" stroke="var(--red)" stroke-width="9"/>
    <path role="img" aria-label="Photo of a frosted pink cupcake topped with a paper heart" d="M0,132 Q130,112 250,126 Q326,205 318,308 Q312,415 258,496 L0,496 Z" fill="url(#photoTone)"/>
  </svg>
  <header class="front-header">
    <span class="brand-name">Tallowmere Financial</span>
    <h1 class="promo-title">Maplebright savings spree!</h1>
  </header>
  <p class="intro">Non-variable rate credit card.<br>There is no intro APR, always a great rate.</p>
  <div class="feature-band"></div>
  <ul class="feature-list">
    <li><svg width="10" height="8" viewBox="0 0 10 8"><path d="M1 4l3 3 5-6" fill="none" stroke="var(--ink)" stroke-width="1.6"/></svg>$0 Balance Transfer Fee, always</li>
    <li><svg width="10" height="8" viewBox="0 0 10 8"><path d="M1 4l3 3 5-6" fill="none" stroke="var(--ink)" stroke-width="1.6"/></svg>Always a fixed low rate,<br>as low as 7.9% APR*</li>
    <li><svg width="10" height="8" viewBox="0 0 10 8"><path d="M1 4l3 3 5-6" fill="none" stroke="var(--ink)" stroke-width="1.6"/></svg>No penalty APR*</li>
    <li><svg width="10" height="8" viewBox="0 0 10 8"><path d="M1 4l3 3 5-6" fill="none" stroke="var(--ink)" stroke-width="1.6"/></svg>$0 Annual Fee</li>
  </ul>
  <p class="savings-copy">Not only could you cut your interest rate in half, but you will also save hundreds of dollars by not paying any balance transfer fees - ever.</p>
  <p class="disclaimer">Annual Percentage Rate. 7.9% is the preferred rate based on qualifying credit.</p>
  <footer class="front-footer">Apply Today! www.tallowmerefin.org</footer>
</section>

<section class="postcard back">
  <div class="tagline-block">When you need OPTIONS,<br>we're here for you</div>
  <div class="brand-block"><span class="brand-name">Tallowmere Financial</span></div>
  <div class="apply-block">Apply Today! www.tallowmerefin.org</div>
  <p class="address">Address<br>1418 W Larkspur Ave. Unit 7,<br>Brookhaven CO 80219</p>
  <p class="phone">
    <svg width="15" height="15" viewBox="0 0 15 15" aria-hidden="true"><rect width="15" height="15" rx="2" fill="var(--grey-text)"/><path d="M4 3.5c.6-.4 1.2-.3 1.5.2l.8 1.4c.2.4 0 .8-.3 1l-.5.4c.5 1.1 1.3 1.9 2.4 2.4l.4-.5c.3-.3.7-.5 1-.3l1.4.8c.5.3.6.9.2 1.5-.6.8-1.5 1-2.4.6C6.4 10.2 4.8 8.6 3.8 6.5c-.4-.9-.6-2.2.2-3z" fill="var(--white)"/></svg>
    555-214-0387
  </p>
  <div class="stamp-box"></div>
  <div class="mail-line" style="top:176px"></div>
  <div class="mail-line" style="top:204px"></div>
  <div class="mail-line" style="top:231px"></div>
  <div class="mail-line" style="top:259px"></div>
  <div class="mail-line" style="top:287px"></div>
</section>

</body>
</html>
```